Design Logo and Business Cards

The job is to design a Logo and Business Cards for a construction company. Please read the requirements carefully.

Logo Requirements

The name of the company is "Vell Building Group". I'd like to see a combination of logos with both the full name, and just "VBG".

Vell Building Group is a building company offering services in both design and construction. We work in both the residential and commercial sectors as follow:

Residential - High end custom construction.
Commercial - fitouts of hotels, bars and restaurants etc

We are after a logo that is mainstream and simple. Would like a few examples using just the letters "VBG" as the main focus point thats eye catching and below it the name Vell building group, as well as examples of just Vell building Group being used. We like rectangular boxes and with the letters or writing inside as well as circles, but are open to anything that's different. We want it to look tidy, sharp, it's not just a logo it's a brand.

Business Card Requirements

Side 1 to feature the logo, side 2 to feature the following at a minimum

Name
Occupation

Phone
Email
Address

Social media

Feel free to jazz up the details using icons (e.g. telephone, envelope, instagram etc)

```html
<!DOCTYPE html>
<html lang="en">
<head>
<meta charset="utf-8">
<title>Vell Building Group – Business Cards</title>
<link rel="stylesheet" href="https://fonts.googleapis.com/css2?family=Lato:wght@400;700;900&display=swap">
<style>
  :root {
    --stage: #3a3b3d;
    --card-white: #ffffff;
    --brand-green: #69be6e;
    --brand-navy: #232a6e;
    --text-navy: #20275f;
  }
  * { box-sizing: border-box; margin: 0; padding: 0; }
  html, body {
    width: 1200px; height: 900px; overflow: hidden;
    background: var(--stage);
    font-family: "Lato", sans-serif;
  }
  .stage { position: relative; width: 1200px; height: 900px; }

  .card {
    position: absolute;
    width: 560px; height: 320px;
    border-radius: 26px;
    overflow: hidden;
  }

  /* Details side */
  .card--details { left: 110px; top: 110px; background: var(--card-white); }
  .card--details .corner-sweep { position: absolute; inset: 0; }
  .name-band {
    position: absolute; left: 0; top: 72px;
    width: 275px; height: 50px;
    background: var(--brand-green);
    clip-path: polygon(0 0, 100% 0, 91% 100%, 0 100%);
  }
  .holder-name {
    position: absolute; left: 36px; top: 70px;
    font-weight: 900; font-size: 23px; letter-spacing: 0.5px;
    color: var(--text-navy);
  }
  .holder-role {
    position: absolute; left: 150px; top: 99px;
    font-weight: 700; font-size: 15px; letter-spacing: 0.6px;
    color: var(--card-white);
  }
  .contact-list { position: absolute; left: 48px; top: 158px; list-style: none; }
  .contact-item {
    display: flex; align-items: center;
    height: 46px;
    font-size: 15px; font-weight: 700;
    color: var(--text-navy);
  }
  .contact-item svg { width: 26px; height: 26px; margin-right: 36px; flex: none; }
  .social-row {
    position: absolute; left: 322px; top: 174px;
    display: flex; gap: 12px;
  }
  .social-dot {
    width: 18px; height: 18px; border-radius: 50%;
    background: var(--brand-navy);
  }

  /* Logo side */
  .card--brand {
    left: 530px; top: 470px;
    background: var(--brand-green);
    display: flex; flex-direction: column; align-items: center; justify-content: center;
  }
  .brand-mark {
    width: 74px; height: 74px; border-radius: 50%;
    background: var(--brand-navy);
    margin-bottom: 22px;
  }
  .brand-name {
    font-weight: 700; font-size: 30px;
    color: var(--brand-navy);
  }
</style>
</head>
<body>
<main class="stage">

  <section class="card card--details" aria-label="Business card, contact side">
    <svg class="corner-sweep" viewBox="0 0 560 320" aria-hidden="true">
      <path d="M372 0 Q420 125 560 205 L560 0 Z" fill="var(--brand-green)"/>
      <path d="M356 -4 Q404 128 566 220" fill="none" stroke="var(--brand-navy)" stroke-width="8"/>
    </svg>
    <div class="name-band"></div>
    <h1 class="holder-name">MARK DALTON</h1>
    <p class="holder-role">DIRECTOR</p>

    <ul class="contact-list">
      <li class="contact-item">
        <svg viewBox="0 0 24 24" aria-hidden="true"><rect x="6" y="2" width="12" height="20" rx="2" fill="none" stroke="var(--brand-navy)" stroke-width="2.4"/><rect x="8.5" y="5" width="7" height="11" fill="var(--brand-navy)"/></svg>
        <span>+98 000 444 31</span>
      </li>
      <li class="contact-item">
        <svg viewBox="0 0 24 24" aria-hidden="true"><rect x="2" y="5" width="20" height="14" rx="1.5" fill="none" stroke="var(--brand-navy)" stroke-width="2.4"/><path d="M3 6 L12 13 L21 6" fill="none" stroke="var(--brand-navy)" stroke-width="2.4"/></svg>
        <span>mark41@vmail.com</span>
      </li>
      <li class="contact-item">
        <svg viewBox="0 0 24 24" aria-hidden="true"><path d="M12 2 C7.6 2 5 5.2 5 9 C5 14 12 22 12 22 C12 22 19 14 19 9 C19 5.2 16.4 2 12 2 Z" fill="var(--brand-navy)"/><circle cx="12" cy="9" r="2.6" fill="var(--card-white)"/></svg>
        <span>Harbor city</span>
      </li>
    </ul>

    <div class="social-row" aria-label="Social media">
      <span class="social-dot"></span>
      <span class="social-dot"></span>
      <span class="social-dot"></span>
    </div>
  </section>

  <section class="card card--brand" aria-label="Business card, logo side">
    <div class="brand-mark" aria-hidden="true"></div>
    <p class="brand-name">Vell Building Group</p>
  </section>

</main>
</body>
</html>
```